Business Card/ Email Signature Design Project

I am an Interior Designer. I need a business card that looks sophisticated stylish but simple in design. My work covers space design/ interior architecture/ furniture design/ product development & styling.

I have a very specific brief and know mostly what I want. I'm hoping to work with someone who can translate my ideas.

My branding should have a strong focus on my name, the majority of my work is referral based.
I'm keen to keep a monochromatic colour scheme: dark charcoal/ black/ white/ embossing/ silver. I'm not suggesting we use all that I've listed, they are possible ideas at this stage. I will need to be mindful of printing costs an also how I make the design work across, cards, letter heads, email logo and web design.

Theory behind images sent below;
1-Rug Image_(minus boarder) I was thinking this image could be used on the back of the card with my contact details over. I like that the lines are almost hand drawn and start to look free form. It's a subtle contrast to a more formal front of the card with my name.
2_Owen Ratley_I really like the orientation, the proportion of font on the card, the colour and the font. I like the lower case for my name and the upper case for 'Interior Design'. Not sure if it should be 'Interior Designer or Interior Design' at this stage, was leaning towards 'Interior Design'. Was thinking the 'i' and 'd' in my surname could be the colour eg 'silver'?? We can decide on this once we see it.

Look forward to hearing from you.
Cheers,
Noreen Bastoli

Industry/Entity Type

Printing

Logo Text

Noreen Bastoli Interior Design

```html
<!DOCTYPE html>
<html lang="en">
<head>
<meta charset="utf-8">
<title>Noreen Bastoli Interior Design – Business Card</title>
<link rel="stylesheet" href="https://fonts.googleapis.com/css2?family=Inter:wght@100;200;300&display=swap">
<style>
  :root {
    --backdrop: #e9e7e4;
    --card-dark: #161616;
    --card-mid: #262626;
    --card-light: #3a3a3a;
    --name-ink: #cfcfcf;
    --tagline-ink: #7c7c7c;
    --contact-ink: #8a8a8a;
  }
  * { box-sizing: border-box; margin: 0; padding: 0; }
  html, body {
    width: 1200px;
    height: 750px;
    overflow: hidden;
    background: var(--backdrop);
  }
  .stage {
    position: relative;
    width: 1200px;
    height: 750px;
  }
  .card {
    position: absolute;
    overflow: hidden;
    font-family: "Inter", "Helvetica Neue", Arial, sans-serif;
  }
  .card--front {
    left: 77px;
    top: 48px;
    width: 678px;
    height: 398px;
    background: var(--card-dark);
  }
  .card-front__texture {
    position: absolute;
    inset: 0;
    background:
      radial-gradient(ellipse at 50% 45%, var(--card-mid) 0%, var(--card-dark) 75%);
  }
  .card-front__identity {
    position: absolute;
    left: 113px;
    top: 140px;
    width: 460px;
  }
  .card-front__name {
    display: block;
    font-weight: 100;
    font-size: 66px;
    line-height: 1;
    letter-spacing: -0.5px;
    color: var(--name-ink);
    white-space: nowrap;
  }
  .card-front__tagline {
    display: block;
    margin-top: 10px;
    font-weight: 200;
    font-size: 19px;
    letter-spacing: 14.6px;
    color: var(--tagline-ink);
    text-transform: uppercase;
    white-space: nowrap;
  }
  .card--back {
    left: 490px;
    top: 333px;
    width: 632px;
    height: 364px;
    background:
      radial-gradient(ellipse at 50% 25%, var(--card-light) 0%, var(--card-mid) 45%, var(--card-dark) 100%);
  }
  .card-back__contact {
    position: absolute;
    left: 40px;
    top: 210px;
    list-style: none;
    font-weight: 200;
    font-size: 26px;
    line-height: 29.5px;
    letter-spacing: -0.3px;
    color: var(--contact-ink);
    text-transform: uppercase;
    white-space: nowrap;
  }
</style>
</head>
<body>
  <main class="stage">
    <section class="card card--front" aria-label="Business card front">
      <div class="card-front__texture" role="img" aria-label="Subtle dark rug pattern of loosely drawn hexagonal lines"></div>
      <div class="card-front__identity">
        <span class="card-front__name">noreen bastoli</span>
        <span class="card-front__tagline">Interior Design</span>
      </div>
    </section>

    <section class="card card--back" aria-label="Business card back">
      <ul class="card-back__contact">
        <li>P.O Box 214 Elmsworth VIC. 3090</li>
        <li>interiors@noreenbastoli.com</li>
        <li>www.noreenbastoli.com</li>
        <li>0400-555-017</li>
      </ul>
    </section>
  </main>
</body>
</html>
```